Bloom Where You Stand redesign book cover

A new cover for my already published book. The old cover looks great but not for a women’s self help book. Cover is killing sales. Once I explain the book it sells quickly AND gets 5 star reviews. Outside of actually explaining the book the cover scares people away. I need a new cover. ASAP! Before The yr end please.
The tag line -
Explore 10 Gentle Steps To Trade Anxious Worry For Quiet Trust And Hope In Every Season. This is a self help book for women 35-45 Christian but not religious. Each chapter is a hands on spiritual experience where the reader takes small tests about themselves, discover why they have negative thoughts, what they are and how to listen to God through hands on methods of listening. NOT strange type of things. They learn what 4 voices they are listening to and how to hone in on Jesus voice. There are scriptures to pray and journaling assignments. The old cover is in the brief with the write up for the back of the book. Please use the new author picture, Publishers logo (tree), barcode, and contact info from the back of the book. And yes the author name and title of the book on the spine. Lay out on the back cover needs to be interesting. You have all the info have fun with it.

Target Market(s)

Women 35-45 yrs old Christian and new believers or seekers.

Industry/Entity Type

Non profit organization. Missionary

Requirements
Must have
• Something DIFFERENT than what is there now. Something inviting. Fresh clear title
Nice to have
• Multi colors however a white stand out cover is also good.
Should not have
• Heavy religious feeling. No church steeples, Jesus faces.

```html
<!DOCTYPE html>
<html lang="en">
<head>
<meta charset="utf-8">
<title>Bloom Where You Stand — Book Cover</title>
<link rel="stylesheet" href="https://fonts.googleapis.com/css2?family=Josefin+Sans:wght@400;700&display=swap">
<style>
  :root {
    --stage: #e6e6e6;
    --paper: #ffffff;
    --ink: #111111;
    --gold: #a8991c;
    --meadow-light: #c9c98a;
    --meadow: #7f9a3a;
    --meadow-deep: #3f5a1e;
    --shade: #141410;
    --author: #ffffff;
  }
  * { margin: 0; padding: 0; box-sizing: border-box; }
  html, body {
    width: 1200px;
    height: 718px;
    overflow: hidden;
    background: var(--stage);
  }
  .stage {
    width: 1200px;
    height: 718px;
    display: flex;
    align-items: center;
    justify-content: center;
  }
  .book-cover {
    position: relative;
    width: 454px;
    height: 680px;
    background: var(--paper);
    overflow: hidden;
    font-family: "Josefin Sans", sans-serif;
    box-shadow: 0 4px 18px rgba(0,0,0,0.18);
  }
  .cover-photo {
    position: absolute;
    left: 0;
    right: 0;
    top: 205px;
    bottom: 0;
    background:
      radial-gradient(ellipse 42% 40% at 50% 42%, rgba(214,168,140,0.55), rgba(214,168,140,0) 70%),
      linear-gradient(180deg,
        var(--paper) 0%,
        #f3f1e4 12%,
        var(--meadow-light) 34%,
        var(--meadow) 52%,
        var(--meadow-deep) 72%,
        #23240f 88%,
        var(--shade) 100%);
  }
  .title-block {
    position: absolute;
    top: 74px;
    left: 0;
    right: 0;
    text-align: center;
    text-transform: uppercase;
  }
  .title-lead {
    display: block;
    color: var(--ink);
    font-weight: 700;
    font-size: 40px;
    line-height: 40px;
    letter-spacing: 1px;
  }
  .title-main {
    display: block;
    color: var(--gold);
    font-weight: 700;
    font-size: 62px;
    line-height: 64px;
    margin-top: 4px;
    white-space: nowrap;
  }
  .tagline {
    margin-top: 14px;
    color: var(--ink);
    font-weight: 400;
    font-size: 12.5px;
    line-height: 15px;
    letter-spacing: 0.5px;
  }
  .author {
    position: absolute;
    left: 0;
    right: 0;
    bottom: 30px;
    text-align: center;
    color: var(--author);
    font-weight: 700;
    font-size: 18px;
    letter-spacing: 5px;
    text-transform: uppercase;
  }
</style>
</head>
<body>
<main class="stage">
  <section class="book-cover">
    <div class="cover-photo" role="img" aria-label="Photograph of a smiling woman with long brown hair looking upward, hand resting on her shoulder, in a sunlit green meadow with soft bokeh light"></div>
    <header class="title-block">
      <h1>
        <span class="title-lead">Bloom Where</span>
        <span class="title-main">You Stand</span>
      </h1>
      <p class="tagline">Explore 10 gentle steps to trade anxious<br>worry for quiet trust and hope<br>in every season</p>
    </header>
    <p class="author">Dana Whitfield</p>
  </section>
</main>
</body>
</html>
```